Ember needs a new design we have an updated logo and want a high qualitative high end feel

feel and aesthetic should be high qualitative like the packaging in a zelvo or the qualatative weight/feel of an zelvo design. modern, elegant bold.probably just the ember logo on the backone vesion could be blue background white letter ... open to ideas
legal, insurance , medical, finance vantor 300
Information Technology
Serif

```html
<!DOCTYPE html>
<html lang="en">
<head>
<meta charset="utf-8">
<title>Ember – Business Card</title>
<link rel="stylesheet" href="https://fonts.googleapis.com/css2?family=Source+Sans+3:wght@400;600&display=swap">
<style>
  :root {
    --ember-blue: #2591cc;
    --ember-blue-light: #2a9ad6;
    --card-white: #f4f4f4;
    --ink: #1f1f1f;
    --backdrop: #d9d9d9;
    --paper: #ffffff;
  }
  * { box-sizing: border-box; margin: 0; padding: 0; }
  html, body {
    width: 1200px; height: 1021px; overflow: hidden;
    background: var(--backdrop);
    font-family: "Source Sans 3", "Myriad Pro", Arial, sans-serif;
  }
  .stage {
    width: 1200px; height: 1021px;
    display: flex; align-items: center; justify-content: center; gap: 80px;
  }
  .card {
    width: 380px; height: 665px; border-radius: 26px;
    position: relative;
    box-shadow: 0 10px 28px rgba(0,0,0,0.18);
  }
  /* Front */
  .card--front {
    background: var(--card-white);
    display: flex; flex-direction: column; align-items: center;
    padding: 70px 40px 60px;
  }
  .person { text-align: center; }
  .person__name {
    color: var(--ember-blue); font-weight: 600; font-size: 25px;
    letter-spacing: 0.3px; text-transform: uppercase;
  }
  .person__title { color: var(--ink); font-size: 20px; margin-top: 2px; }
  .brand-mark {
    margin-top: auto; margin-bottom: auto;
    display: flex; align-items: center; gap: 10px;
    color: var(--ember-blue); font-weight: 600; font-size: 44px;
  }
  .brand-mark__dot {
    width: 14px; height: 14px; border-radius: 50%; background: var(--ember-blue);
  }
  .address { text-align: center; color: var(--ink); font-size: 20px; line-height: 1.25; }
  .divider {
    width: 100%; margin: 18px 0; display: flex; align-items: center; gap: 10px;
  }
  .divider__rule { flex: 1; height: 2px; background: var(--ember-blue); }
  .divider__icons { display: flex; gap: 10px; }
  .divider__icons svg { width: 16px; height: 16px; }
  .contact { text-align: center; font-size: 20px; line-height: 1.3; color: var(--ink); }
  .contact__web { color: var(--ember-blue); }
  /* Back */
  .card--back {
    background: linear-gradient(160deg, var(--ember-blue-light), var(--ember-blue));
    display: flex; align-items: center; justify-content: center;
  }
  .back-name { color: var(--paper); font-size: 76px; font-weight: 400; letter-spacing: 1px; }
</style>
</head>
<body>
<main class="stage">
  <section class="card card--front" aria-label="Card front">
    <div class="person">
      <p class="person__name">Dana Whitlow</p>
      <p class="person__title">Founder/CEO</p>
    </div>
    <div class="brand-mark"><span class="brand-mark__dot"></span><span>ember</span></div>
    <p class="address">850 W Linden Ave Suite 310<br>Fairview, OH 44126</p>
    <div class="divider">
      <span class="divider__rule"></span>
      <span class="divider__icons">
        <svg viewBox="0 0 16 16" fill="none" stroke="#2591cc" stroke-width="1.4"><rect x="4.5" y="1.5" width="7" height="13" rx="1.2"/><line x1="7" y1="12.3" x2="9" y2="12.3"/></svg>
        <svg viewBox="0 0 16 16" fill="none" stroke="#2591cc" stroke-width="1.4"><rect x="1.5" y="3.5" width="13" height="9"/><polyline points="1.5,3.5 8,9 14.5,3.5"/></svg>
        <svg viewBox="0 0 16 16" fill="none" stroke="#2591cc" stroke-width="1.2"><circle cx="8" cy="8" r="6.5"/><ellipse cx="8" cy="8" rx="2.8" ry="6.5"/><line x1="1.5" y1="8" x2="14.5" y2="8"/></svg>
      </span>
      <span class="divider__rule"></span>
    </div>
    <div class="contact">
      <p>(555) 014-7391</p>
      <p>dana@emberhq.com</p>
      <p class="contact__web">www.emberhq.com</p>
    </div>
  </section>
  <section class="card card--back" aria-label="Card back">
    <p class="back-name">ember</p>
  </section>
</main>
</body>
</html>
```